Business Card for Modern Marketing Consultancy

Business card needed for marketing consultancy with existing logo.

Lanternway Group is a specialized boutique marketing consultancy that provides startup, small and mid size consumer businesses thought leadership and implementation of marketing strategies to help your business grow.

Our expertise, experience and industry knowledge stems from some of New York’s top global beauty and retail companies and allows us to draw from an array of successful marketing strategies and growth tactics tailored to suit the needs of your business

lanternwaygroup.com

Target Market(s)

start up, small and mid size consumer packaged goods businesses

Industry/Entity Type

Leadership

Requirements
Must have
• Must have the logo of the business and use of the exact colors of the logo.
Must be simple, sleek, modern and clean. Must make a statement and be eye catching.

Front: looking for unique design or visual statement with logo and tagline

Back of card should have:
logo - if not use on front.
Delia R. Vasquez
Founder
Lanternway Group
m: 646.503.1872
deliavasquez@lanternwaygroup.com
lanternwaygroup.com

Please use the following words as these describe my services:
strategy analytics branding research

Please refer to the website look and feel: lanternwaygroup.com

Please kindly note that I am looking for a unique design that I cannot do myself with a template. thank you.
Nice to have
• Please also try and incorporate additional files attached.

```html
<!DOCTYPE html>
<html lang="en">
<head>
<meta charset="utf-8">
<title>Lanternway Group — Business Card</title>
<link href="https://fonts.googleapis.com/css2?family=Quicksand:wght@400;500;600&display=swap" rel="stylesheet">
<style>
  :root {
    --magenta: #e4237f;
    --magenta-deep: #c8176c;
    --magenta-soft: #ef5aa2;
    --ink-grey: #6b6b6b;
    --text-grey: #8a8a8a;
    --rule-grey: #cfcfcf;
    --paper: #ffffff;
    --backdrop: #d9d9db;
  }
  * { box-sizing: border-box; margin: 0; padding: 0; }
  html, body {
    width: 1200px; height: 900px; overflow: hidden;
    background: var(--backdrop);
    font-family: "Quicksand", sans-serif;
  }
  .sheet {
    width: 1200px; height: 900px;
    display: flex; flex-direction: column;
    align-items: center; justify-content: center; gap: 56px;
  }
  .card {
    position: relative;
    width: 620px; height: 354px;
    border-radius: 26px;
    overflow: hidden;
    box-shadow: 0 6px 18px rgba(0,0,0,0.14);
  }

  /* Front */
  .card-front {
    background: linear-gradient(135deg, var(--magenta-deep), var(--magenta) 55%, var(--magenta-soft));
    color: var(--paper);
  }
  .front-art {
    position: absolute; left: 150px; top: 22px;
    width: 300px; height: 230px; border-radius: 40px;
    background: radial-gradient(ellipse at center, rgba(160,10,80,0.35), rgba(160,10,80,0) 70%);
  }
  .front-brand {
    position: absolute; left: 0; right: 0; top: 118px;
    text-align: center;
  }
  .front-name {
    font-size: 54px; font-weight: 600; letter-spacing: -0.5px; line-height: 1;
  }
  .front-tagline {
    margin-top: 12px;
    font-size: 20px; font-weight: 400; letter-spacing: 1px;
  }
  .services {
    position: absolute; left: 0; right: 0; bottom: 26px;
    display: flex; justify-content: center; align-items: center; gap: 22px;
    font-size: 17px; letter-spacing: 1px;
  }
  .services .dot {
    width: 7px; height: 7px; border-radius: 50%; background: var(--paper);
  }

  /* Back */
  .card-back { background: var(--paper); }
  .back-brand {
    position: absolute; left: 44px; top: 36px;
  }
  .back-name {
    font-size: 46px; font-weight: 600; color: var(--ink-grey); letter-spacing: -0.5px; line-height: 1;
  }
  .back-tagline {
    margin-top: 6px; margin-left: 90px;
    font-size: 17px; color: var(--magenta); letter-spacing: 0.8px;
  }
  .contact {
    position: absolute; left: 200px; top: 124px; width: 300px;
    text-align: center; color: var(--text-grey);
    font-size: 16px; line-height: 1.25;
  }
  .contact .rule {
    border-top: 2px dotted var(--rule-grey); margin: 7px 20px;
  }
  .contact .title { font-size: 14px; }
  .contact .web { color: var(--magenta); }
  .accent-dot {
    position: absolute; width: 9px; height: 9px; border-radius: 50%;
    background: var(--magenta-deep);
  }
</style>
</head>
<body>
<main class="sheet">
  <section class="card card-front" aria-label="Card front">
    <div class="front-art" role="img" aria-label="Faint pair of footprints illustration"></div>
    <div class="front-brand">
      <div class="front-name">Lanternway Group</div>
      <div class="front-tagline">Smarter Marketing for Growth</div>
    </div>
    <div class="services">
      <span>strategy</span><span class="dot"></span>
      <span>analytics</span><span class="dot"></span>
      <span>branding</span><span class="dot"></span>
      <span>research</span>
    </div>
  </section>

  <section class="card card-back" aria-label="Card back">
    <div class="back-brand">
      <div class="back-name">Lanternway Group</div>
      <div class="back-tagline">smarter marketing for growth</div>
    </div>
    <div class="contact">
      <div class="rule"></div>
      <div>Delia R. Vasquez</div>
      <div class="title">Founder</div>
      <div class="rule"></div>
      <div>Lanternway Group</div>
      <div>m: 646.503.1872</div>
      <div>deliavasquez@lanternwaygroup.com</div>
      <div class="rule"></div>
      <div class="web">www.lanternwaygroup.com</div>
      <div class="rule"></div>
    </div>
    <span class="accent-dot" style="left:56px; top:320px;"></span>
    <span class="accent-dot" style="left:150px; top:320px;"></span>
    <span class="accent-dot" style="left:564px; top:320px;"></span>
    <span class="accent-dot" style="left:564px; top:240px;"></span>
    <span class="accent-dot" style="left:564px; top:160px;"></span>
  </section>
</main>
</body>
</html>
```